practice letterhead

I need a letterhead design for a new company that is a veterinary specialty company. I am conservative. I want it to look professional - not "cutesy"

I need my name, credentials, address, phone number and website/email on it.

My personal information is as follows: Marisol Tedder, DVM, DACVIM (Neurology) Certified Veterinary Pain Practitioner (or CVPP) Certified Canine Rehabilitation Therapist (or CCRT) 4170 Larkfield Hwy Walpole, MA 02081 508-347-6620 marisol.tedder@petspineandcare.com www.petspineandcare.com

```html
<!DOCTYPE html>
<html lang="en">
<head>
<meta charset="utf-8">
<title>Practice Letterhead</title>
<link href="https://fonts.googleapis.com/css2?family=Anton&display=swap" rel="stylesheet">
<style>
  :root {
    --canvas: #ffffff;
    --sheet: #ffffff;
    --sheet-edge: #000000;
    --ink: #111111;
    --brand-teal: #6a9585;
    --brand-navy: #1d3a4a;
    --tile-deep: #7fc6ee;
    --tile-light: #d6eefb;
  }
  * { margin: 0; padding: 0; box-sizing: border-box; }
  html, body {
    width: 1200px;
    height: 1000px;
    overflow: hidden;
    background: var(--canvas);
  }
  .canvas {
    position: relative;
    width: 1200px;
    height: 1000px;
  }
  .letterhead {
    position: absolute;
    left: 227px;
    top: 17px;
    width: 748px;
    height: 968px;
    background: var(--sheet);
    border: 3px solid var(--sheet-edge);
    border-radius: 3px;
    overflow: hidden;
    font-family: "Anton", "Arial Narrow", sans-serif;
    color: var(--ink);
  }
  .practice-mark {
    position: absolute;
    right: 36px;
    top: 26px;
    display: flex;
    align-items: center;
    gap: 12px;
  }
  .practice-mark__dot {
    width: 54px;
    height: 54px;
    border-radius: 50%;
    background: var(--brand-navy);
    flex: none;
  }
  .practice-mark__name {
    color: var(--brand-teal);
    font-size: 21px;
    line-height: 1.15;
    letter-spacing: 0.3px;
    width: 250px;
  }
  .sender {
    position: absolute;
    left: 36px;
    top: 90px;
    width: 100px;
    text-align: center;
    font-size: 14px;
    line-height: 21px;
    letter-spacing: 0.3px;
  }
  .corner-texture {
    position: absolute;
    left: 0;
    bottom: 0;
    width: 330px;
    height: 185px;
  }
  .contact-footer {
    position: absolute;
    left: 0;
    right: 0;
    bottom: 16px;
    font-size: 14px;
    line-height: 21px;
    letter-spacing: 0.3px;
  }
  .contact-footer__address {
    text-align: center;
    padding-left: 8px;
  }
  .contact-footer__links {
    display: flex;
    justify-content: center;
    gap: 22px;
    padding-left: 8px;
  }
</style>
</head>
<body>
<div class="canvas">
  <div class="letterhead">
    <div class="practice-mark">
      <span class="practice-mark__dot"></span>
      <span class="practice-mark__name">Harborline Veterinary Spine &amp; Comfort Clinic</span>
    </div>

    <div class="sender">
      <p class="sender__name">Your Name Here</p>
      <p class="sender__credential">Credential</p>
    </div>

    <svg class="corner-texture" viewBox="0 0 330 185" role="img" aria-label="Soft blue mosaic texture in the lower left corner">
      <defs>
        <linearGradient id="tileFade" x1="0" y1="1" x2="1" y2="0">
          <stop offset="0" stop-color="var(--tile-deep)" stop-opacity="0.95"/>
          <stop offset="0.6" stop-color="var(--tile-deep)" stop-opacity="0.55"/>
          <stop offset="1" stop-color="var(--tile-light)" stop-opacity="0.35"/>
        </linearGradient>
      </defs>
      <path d="M0 0 H45 V10 H95 V20 H165 V60 H200 V95 H250 V125 H300 V150 H330 V185 H0 Z" fill="url(#tileFade)"/>
    </svg>

    <div class="contact-footer">
      <p class="contact-footer__address">Your Address Here</p>
      <p class="contact-footer__links">
        <span class="contact-footer__web">www.website.com</span>
        <span class="contact-footer__divider">|</span>
        <span class="contact-footer__email">email@website.com</span>
      </p>
    </div>
  </div>
</div>
</body>
</html>
```